Webdesign für ORVI Registrierung für die USA
Zielgruppe
Erstellung von Reisegenehmigungen (Visa)
Aufgabenstellung
- Orientierung an Orvi.us
- es gibt kein Logo oder CD
- die Webseite soll seriös wirken

```html
<!DOCTYPE html>
<html lang="en">
<head>
<meta charset="utf-8">
<title>ORVI – Travel Authorization for the USA</title>
<link href="https://fonts.googleapis.com/css2?family=Poppins:wght@500;600&family=Raleway:wght@400;500;600;700&display=swap" rel="stylesheet">
<style>
:root{
  --red:#b3121c;
  --red-bright:#d5101c;
  --blue:#0a4fa2;
  --blue-deep:#1f3f96;
  --ink:#333640;
  --ink-soft:#555a63;
  --heading:#4a4c52;
  --line:#dcdde0;
  --footer:#ececee;
  --footer-bar:#dcdcdf;
  --dark:#4b4f55;
  --white:#ffffff;
}
*{box-sizing:border-box;margin:0;padding:0}
html,body{width:1200px;height:3367px;overflow:hidden}
body{font-family:"Raleway",sans-serif;color:var(--ink);background:var(--white);position:relative}
.btn{display:inline-block;border-radius:20px;font-family:"Raleway",sans-serif;font-weight:600;text-decoration:none;text-align:center;text-transform:uppercase}
.btn-red{background:var(--red);color:var(--white);box-shadow:0 4px 8px rgba(0,0,0,.18)}

/* hero */
.hero{position:absolute;left:0;top:0;width:1200px;height:537px;overflow:hidden}
.hero-bg{position:absolute;inset:0;background:linear-gradient(100deg,#1f3f9a 0%,#3550a6 35%,#7a3f8a 58%,#c01a2c 80%,#c8101f 100%)}
.nav{position:absolute;left:98px;right:98px;top:26px;height:30px;display:flex;align-items:center}
.logo{font-family:"Raleway",sans-serif;font-weight:700;font-size:30px;letter-spacing:2px;color:var(--white)}
.nav-links{margin-left:auto;display:flex;align-items:center;gap:37px;list-style:none}
.nav-links a{color:var(--white);text-decoration:none;font-size:13px;font-weight:500}
.nav-links .btn{background:var(--blue);padding:7px 20px;font-size:12px;margin-left:18px}
.hero h1{position:absolute;left:0;width:1200px;top:160px;text-align:center;font-family:"Poppins",sans-serif;font-weight:600;font-size:28px;color:var(--white)}
.hero .lead{position:absolute;left:260px;width:680px;top:218px;text-align:center;color:var(--white);font-size:14.5px;line-height:21px;font-weight:500}
.feature{position:absolute;top:330px;width:220px;text-align:center}
.feature .pic{width:116px;height:116px;margin:0 auto;border-radius:50%;border:2px solid rgba(255,255,255,.55)}
.feature .label{margin-top:24px;color:var(--white);font-size:14.5px;letter-spacing:2px;font-weight:500}

/* eligibility */
.plane{position:absolute;left:170px;top:625px;width:137px;height:133px;border-radius:12px;background:linear-gradient(135deg,#f3d25a 0%,#e9ebef 40%,#d9dbe0 100%)}
.elig{position:absolute;left:399px;top:618px;width:704px}
.elig h2{font-weight:700;font-size:29px;color:var(--heading);letter-spacing:.3px}
.rule{width:44px;height:2px;background:var(--red);margin:16px 0 19px}
.elig p{font-size:14.5px;line-height:21px;color:var(--ink-soft);margin-bottom:21px}
.elig .btn{padding:8px 24px;font-size:12px;font-weight:500;margin-top:12px}

.band{position:absolute;left:99px;top:978px;width:1002px;height:76px;background:var(--blue);display:flex;align-items:center;justify-content:center;font-size:23px;color:rgba(255,255,255,.6)}
.band b{font-weight:500;color:var(--white);margin-left:6px}

/* cards */
.card{position:absolute;top:1144px;width:316px;height:379px;border:1px solid var(--line);text-align:center;padding:0 36px}
.card.active{border-color:var(--blue)}
.card h3{font-weight:600;font-size:18px;line-height:22px;color:var(--ink);margin-top:24px;text-transform:uppercase}
.card.active h3{color:var(--blue);text-decoration:underline}
.card p{font-size:13px;line-height:21px;color:var(--ink-soft);margin-top:16px}
.card .btn{position:absolute;left:50%;bottom:-20px;transform:translateX(-50%);width:150px;height:40px;line-height:38px;font-size:12px;letter-spacing:1.5px;background:var(--white);border:2px solid #c8c9cc;color:var(--ink)}
.card.active .btn{background:var(--red);border-color:var(--red);color:var(--white)}
.icon-ph{width:70px;height:70px;border-radius:8px;margin:66px auto 0;background:linear-gradient(135deg,#f1dadd,#dfe4f1)}

.divider{position:absolute;left:99px;top:1630px;width:1002px;height:1px;background:var(--line)}

/* status columns */
.col{position:absolute;top:1714px;width:470px}
.col-left{left:99px}
.col-right{left:613px}
.col h2{font-weight:700;font-size:23px;line-height:30px;color:var(--red-bright)}
.col h2 span{color:var(--blue)}
.col p{font-size:14.5px;line-height:21px;color:var(--ink-soft);margin-top:30px}
.ticks{list-style:none;margin-top:20px}
.ticks li{display:flex;align-items:center;font-size:14px;color:var(--ink-soft);height:28px}
.ticks svg{margin-right:9px;flex:none}
.ticks small{font-size:11px;color:#888;margin-left:4px}
.col .btn{padding:8px 20px;font-size:12px;font-weight:500;margin-top:20px}
.col-right p.after{margin-top:18px}

/* dark */
.dark{position:absolute;left:0;top:2259px;width:1200px;height:491px;background:var(--dark);text-align:center;color:var(--white)}
.dark h2{font-weight:700;font-size:29px;margin-top:88px}
.dark .rule{margin:16px auto 18px;background:var(--red-bright)}
.dark p{width:1000px;margin:0 auto 21px;font-size:14.5px;line-height:21px;font-weight:500}

/* cta */
.cta{position:absolute;left:0;top:2820px;width:1200px;text-align:center}
.cta h2{font-weight:700;font-size:29px;color:var(--heading);letter-spacing:.3px}
.cta p{width:740px;margin:18px auto 0;font-size:14.5px;line-height:21px;color:var(--ink-soft)}
.cta .btn{margin-top:27px;width:150px;height:40px;line-height:40px;font-size:12px;letter-spacing:1.5px}

/* footer */
.footer{position:absolute;left:0;top:3072px;width:1200px;height:244px;background:var(--footer)}
.foot-links{position:absolute;left:98px;top:85px;display:grid;grid-template-columns:163px 120px;row-gap:14px;list-style:none}
.foot-links a{font-size:12px;color:var(--ink-soft);text-decoration:none}
.help{position:absolute;right:99px;top:84px;text-align:right}
.help .q{font-size:13px;font-weight:600;color:var(--ink)}
.help .hours{font-size:11px;color:var(--ink-soft);margin-top:6px}
.help .tel{font-size:13px;font-weight:600;color:var(--ink)}
.help .tel span{font-size:18px;font-weight:500;color:var(--blue)}
.cards{display:flex;justify-content:flex-end;gap:8px;margin-top:12px}
.cards i{display:block;width:45px;height:28px;border-radius:3px}
.bottom{position:absolute;left:0;top:3316px;width:1200px;height:51px;background:var(--footer-bar)}
.bottom p{position:absolute;left:99px;top:19px;font-size:11.5px;color:var(--ink-soft)}
.social{position:absolute;right:99px;top:17px;display:flex;gap:16px}
.social i{display:block;width:16px;height:16px;border-radius:50%;background:#8a8c91}
</style>
</head>
<body>

<header class="hero">
  <div class="hero-bg" role="img" aria-label="Waving American flag in blue and red"></div>
  <nav class="nav">
    <div class="logo">ORVI</div>
    <ul class="nav-links">
      <li><a href="#">VISA BUSINESS</a></li>
      <li><a href="#">VISA WHAT IS ETA</a></li>
      <li><a href="#">CONTACT</a></li>
      <li><a class="btn" href="#">APPLY NOW</a></li>
    </ul>
  </nav>
  <h1>Beguiled &amp; demoralized by the charms of pleasure moment.</h1>
  <p class="lead">dignissimos ducimus qui blanditiis praesentium voluptatum deleniti atque corrupti quos dolores et quas molestias excepturi sint occaecati cupiditate non provident.</p>
  <div class="feature" style="left:204px">
    <div class="pic" role="img" aria-label="Illustration of a laptop with a search glass" style="background:radial-gradient(circle at 45% 55%,#4fb8d8 0 30%,#e8e2d6 31% 60%,transparent 61%)"></div>
    <div class="label">APPLY ONLINE</div>
  </div>
  <div class="feature" style="left:477px">
    <div class="pic" role="img" aria-label="Illustration of a globe with suitcase and airplane" style="background:radial-gradient(circle at 50% 55%,#f0a82a 0 22%,#3f8fd6 23% 48%,transparent 49%)"></div>
    <div class="label">TRAVEL TO THE U.S</div>
  </div>
  <div class="feature" style="left:750px">
    <div class="pic" role="img" aria-label="Illustration of passports and a ticket" style="background:radial-gradient(circle at 40% 60%,#e05a2a 0 25%,#3c6fc0 26% 45%,transparent 46%)"></div>
    <div class="label">IMMIGRATION</div>
  </div>
</header>

<div class="plane" role="img" aria-label="Line illustration of an airplane under the sun"></div>
<section class="elig">
  <h2>FREE ORVI ELIGIBILITY TEST</h2>
  <div class="rule"></div>
  <p>Only citizens of Visa Waiver Countries are allowed to apply for ORVI. It is important to know if you qualify for ORVI before you submit your application. Use the drop-down menu on the left to select your nationality and click on "Submit".</p>
  <p>The ORVI application system is entirely online. There are no forms that need to be printed and you do not have to go to a U.S. Embassy or Consulate in person. Download the ORVI Application Guide and apply today!.</p>
  <a class="btn btn-red" href="#">APPLY NOW</a>
</section>

<div class="band">Please submit the form contact us via email at: <b>info@orvi.us</b></div>

<article class="card" style="left:99px">
  <div class="icon-ph" role="img" aria-label="Line icon of speech bubbles"></div>
  <h3>What is ORVI?</h3>
  <p>ORVI stands for Online Registration for Visitor Information. ORVI is an online application system developed by the United States government to. . .</p>
  <a class="btn" href="#">READ MORE</a>
</article>
<article class="card active" style="left:442px">
  <div class="icon-ph" role="img" aria-label="Line icon of a handshake"></div>
  <h3>Who needs to apply<br>for ORVI?</h3>
  <p>All travelers entering the United States (by air or sea) under the visa waiver program are required to hold a valid. . .</p>
  <a class="btn" href="#">READ MORE</a>
</article>
<article class="card" style="left:784px">
  <div class="icon-ph" role="img" aria-label="Line icon of an identity document"></div>
  <h3>What is the visa waiver program?</h3>
  <p>The visa waiver program is a U.S. govern­ment program that enables citizens and nationals from the Visa Waiver. . .</p>
  <a class="btn" href="#">READ MORE</a>
</article>

<div class="divider"></div>

<section class="col col-left">
  <h2>Verify - Locate - Check<br>Status of your <span>ORVI</span> Travel Authorization</h2>
  <p>Do you already have an existing travel authorization but got questions? We can assist you with the following:</p>
  <ul class="ticks">
    <li><svg width="17" height="17" viewBox="0 0 17 17" fill="none" stroke="#0a4fa2" stroke-width="1.6"><path d="M15 8.5A6.5 6.5 0 1 1 11 2.5"/><path d="M5 8l3 3 8-8"/></svg>Receive help to verify your ORVI</li>
    <li><svg width="17" height="17" viewBox="0 0 17 17" fill="none" stroke="#0a4fa2" stroke-width="1.6"><path d="M15 8.5A6.5 6.5 0 1 1 11 2.5"/><path d="M5 8l3 3 8-8"/></svg>Receive help to locate your existing travel authorization (ORVI)</li>
    <li><svg width="17" height="17" viewBox="0 0 17 17" fill="none" stroke="#0a4fa2" stroke-width="1.6"><path d="M15 8.5A6.5 6.5 0 1 1 11 2.5"/><path d="M5 8l3 3 8-8"/></svg>Check the status of your travel authorization</li>
  </ul>
  <a class="btn btn-red" href="#">CONTINUE</a>
</section>

<section class="col col-right">
  <h2>Update an existing ORVI<br>before flying to the <span>United States</span></h2>
  <p>Travelers with an approved travel authorization (ORVI) may update their own travel authorization before each trip to the United States. The following information can be changed before each trip:</p>
  <ul class="ticks">
    <li><svg width="17" height="17" viewBox="0 0 17 17" fill="none" stroke="#0a4fa2" stroke-width="1.6"><path d="M15 8.5A6.5 6.5 0 1 1 11 2.5"/><path d="M5 8l3 3 8-8"/></svg>Email address</li>
    <li><svg width="17" height="17" viewBox="0 0 17 17" fill="none" stroke="#0a4fa2" stroke-width="1.6"><path d="M15 8.5A6.5 6.5 0 1 1 11 2.5"/><path d="M5 8l3 3 8-8"/></svg>Telephone number</li>
    <li><svg width="17" height="17" viewBox="0 0 17 17" fill="none" stroke="#0a4fa2" stroke-width="1.6"><path d="M15 8.5A6.5 6.5 0 1 1 11 2.5"/><path d="M5 8l3 3 8-8"/></svg>Airline you are flying with</li>
    <li><svg width="17" height="17" viewBox="0 0 17 17" fill="none" stroke="#0a4fa2" stroke-width="1.6"><path d="M15 8.5A6.5 6.5 0 1 1 11 2.5"/><path d="M5 8l3 3 8-8"/></svg>Flight number</li>
    <li><svg width="17" height="17" viewBox="0 0 17 17" fill="none" stroke="#0a4fa2" stroke-width="1.6"><path d="M15 8.5A6.5 6.5 0 1 1 11 2.5"/><path d="M5 8l3 3 8-8"/></svg>City where you are boarding</li>
    <li><svg width="17" height="17" viewBox="0 0 17 17" fill="none" stroke="#0a4fa2" stroke-width="1.6"><path d="M15 8.5A6.5 6.5 0 1 1 11 2.5"/><path d="M5 8l3 3 8-8"/></svg>Address while in the United States<small>(unless if transit through the U.S.)</small></li>
  </ul>
  <p class="after">We can assist you in updating and verifying your travel authorization before departure.</p>
  <a class="btn btn-red" href="#">UPDATE ORVI</a>
</section>

<section class="dark" role="img" aria-label="Dimmed photo of an office background">
  <h2>UNDERTAKES LABORIOUS PHYSICAL EXERCISE</h2>
  <div class="rule"></div>
  <p>At vero eos et accusamus et iusto odio dignissimos ducimus qui blanditiis praesentium voluptatum deleniti atque corrupti quos dolores et quas molestias excepturi sint occaecati cupiditate non provident, similique sunt in culpa qui officia deserunt mollitia animi, id est laborum et dolorum fuga. Et harum quidem rerum facilis est et expedita distinctio. Nam libero tempore, cum soluta nobis est eligendi optio cumque nihil impedit quo minus id quod maxime placeat facere possimus, omnis voluptas assumenda est, omnis dolor repellendus. Temporibus autem quibusdam et aut officiis debitis aut rerum necessitatibus saepe eveniet ut et voluptates repudiandae sint et molestiae non recusandae. Itaque earum rerum hic tenetur a sapiente delectus, ut aut reiciendis voluptatibus maiores alias consequatur aut perferendis doloribus asperiores repellat.</p>
  <p>On the other hand, we denounce with righteous indignation and dislike men who are so beguiled and demoralized by the charms of pleasure of the moment, so blinded by desire, that they cannot foresee the pain and trouble that are bound to ensue; and equal blame belongs to those who fail in their duty through weakness of will, which is the same as saying through shrinking from toil and pain. These cases are perfectly simple and easy to distinguish. In a free hour, when our power of choice is untrammelled and when nothing prevents our being able to do what we like best, every pleasure is to be welcomed and every pain avoided.</p>
</section>

<section class="cta">
  <h2>DUCIMUS QUI BLANDITIIS PRAESENTIUM</h2>
  <p>Righteous indignation and dislike men who are so beguiled and demoralized by the charms of pleasure of the moment, so blinded by desire</p>
  <a class="btn btn-red" href="#">APPLY NOW</a>
</section>

<footer class="footer">
  <ul class="foot-links">
    <li><a href="#">START PAGE</a></li><li><a href="#">WHAT IS ETA</a></li>
    <li><a href="#">TOURIST VISA</a></li><li><a href="#">CONDITIONS</a></li>
    <li><a href="#">BUSINESS VISA</a></li><li><a href="#">CONTACT</a></li>
  </ul>
  <div class="help">
    <div class="q">Sie Brauchen Hilfe?</div>
    <div class="hours">Service Hotline Von Mo-Fr 10-16 Uhr</div>
    <div class="tel">Kostenfrei: <span>0800 555 01234</span></div>
    <div class="cards">
      <i style="background:#2a6fc0"></i>
      <i style="background:#d8452a"></i>
      <i style="background:#ffffff"></i>
    </div>
  </div>
</footer>
<div class="bottom">
  <p>© 2017 ORVI, ALL RIGHTS RESERVED</p>
  <div class="social"><i></i><i></i><i></i></div>
</div>

</body>
</html>
```